Broschüre
Zielgruppe
Wir sind eine ambulanter Pflegedienst in Rostock. Ab dem Herbst 25 bieten wir für Interessenten mit einem Pflegegrad begleitete reisen an. Eine Fachkraft wird Patienten mit Pflegegrad in kleinen Gruppen begleiten. Den Text für den Flyer haben wir eingefügt. Bitte die Bider aus dem Stock Portal wählen. Über den Flyer sollen Patienten gefunden werden.
Der Flyer
sollte Serios wirken und Reiselust der Senioren wecken.
Aufgabenstellung
Hier der Text für den Flyer:
Was wir bieten:
✔️ Begleitung durch erfahrene Pflegefachkräfte ✔️ Körperpflege, Medikamentengabe & Betreuung wie zuhause ✔️ 24-Stunden-Erreichbarkeit unserer Pflegekräfte vor Ort im gebuchten Hotel ✔️ Zusammenarbeit mit ausgewählten Hotels – barrierefrei & seniorengerecht ✔️ Kleine Gruppen & individuelle Betreuung vor Ort
Gut zu wissen:
Für unsere pflegerische Begleitung entstehen Ihnen keine zusätzlichen Kosten, wenn Sie einen Pflegegrad haben und das Verhinderungspflege-Budget noch nicht aufgebraucht ist.
Lediglich die Hotelkosten sind von Ihnen selbst zu tragen.
Wer hat Anspruch auf Verhinderungspflege?
Alle Pflegebedürftigen mit einem anerkannten Pflegegrad ab Stufe 2 können jährlich Verhinderungspflege über die Pflegekasse abrufen – ideal, um sich im Urlaub sicher begleiten zu lassen!
Unser Service – Ihr Mehrwert:
Wir organisieren Ihre Reise von A bis Z und begleiten Sie oder Ihre Angehörigen auf dem Weg zu Erholung und neuen Eindrücken – mit Herz, Kompetenz und Erfahrung. Vor Ort sind müssen Sie auf nichts verzichten und werden versorgt wie zu Hause. Gerne organisieren wir auch die Abholung aus ihrer Hässlichkeit.
???? Sonnenweg Touren – Ihr verlässlicher Partner für Pflege und Lebensfreude
???? Jetzt informieren & Platz sichern: 0381 - 72946183
???? Mail@sonnenweg-touren .de
???? www.sonnenweg-touren.de

```html
<!DOCTYPE html>
<html lang="de">
<head>
<meta charset="utf-8">
<title>Sonnenweg Touren – Flyer</title>
<link rel="stylesheet" href="https://fonts.googleapis.com/css2?family=Plus+Jakarta+Sans:wght@400;500;700;800&display=swap">
<style>
  :root {
    --navy: #1b2348;
    --blue: #2580c8;
    --blue-light: #5aa6e6;
    --page-grey: #f5f5f7;
    --white: #ffffff;
  }
  * { box-sizing: border-box; margin: 0; padding: 0; }
  html, body { width: 1200px; height: 960px; overflow: hidden; background: var(--white); }
  body { position: relative; font-family: "Plus Jakarta Sans", sans-serif; color: var(--navy); }

  .page { position: absolute; top: 151px; width: 465px; height: 656px; background: var(--white); overflow: hidden; box-shadow: 0 6px 24px rgba(0,0,0,0.07); }
  .page--front { left: 98px; }
  .page--back { left: 634px; background: var(--page-grey); }

  .hero-photo { position: absolute; inset: 0; }
  .hero-bubble { position: absolute; left: 0; top: 0; }

  .headline { position: absolute; white-space: nowrap; font-weight: 800; line-height: 1; }
  .headline__reiselust { left: 230px; top: 379px; font-size: 31px; color: var(--white); letter-spacing: -0.3px; }
  .headline__trotz { left: 277px; top: 413px; font-size: 21px; color: var(--navy); }
  .headline__pflegegrad { left: 228px; top: 434px; font-size: 30px; color: var(--navy); letter-spacing: -0.3px; }
  .headline__rule { position: absolute; left: 288px; top: 487px; width: 49px; height: 3px; background: var(--white); }
  .headline__promise { left: 240px; top: 496px; font-size: 21px; color: var(--white); font-weight: 700; line-height: 24px; text-align: right; }

  .badge { position: absolute; left: 373px; top: 337px; width: 80px; height: 80px; border-radius: 50%; background: var(--navy); color: var(--white); text-align: center; font-weight: 700; font-size: 14px; line-height: 17px; padding-top: 14px; }
  .badge__neu { color: var(--blue-light); }

  .footer { position: absolute; left: 36px; top: 605px; display: flex; align-items: center; width: 400px; }
  .footer__dot { width: 36px; height: 36px; border-radius: 50%; background: var(--blue); margin-right: 9px; flex: none; }
  .footer__name { font-size: 18px; font-weight: 700; color: var(--navy); white-space: nowrap; }
  .footer__url { margin-left: auto; font-size: 11px; font-weight: 500; color: #111; }

  .back-curve { position: absolute; left: 0; top: 0; }
  .block { position: absolute; left: 40px; width: 385px; }
  .block h2 { font-size: 14px; font-weight: 800; line-height: 16px; }
  .block p { font-size: 11px; line-height: 14.5px; font-weight: 400; }

  .offers { list-style: none; position: absolute; left: 40px; top: 62px; width: 360px; }
  .offers li { position: relative; padding-left: 18px; font-size: 11px; line-height: 14.5px; margin-bottom: 5.5px; }
  .offers svg { position: absolute; left: 0; top: 3px; }

  .contact { position: absolute; left: 40px; top: 504px; font-size: 11px; line-height: 20px; }
  .contact span { display: inline-block; width: 52px; }

  .cta { position: absolute; left: 292px; top: 485px; width: 108px; height: 89px; border-radius: 50%; background: var(--blue); color: var(--white); font-weight: 700; font-size: 11.5px; line-height: 15.5px; text-align: center; padding-top: 13px; }
</style>
</head>
<body>

<section class="page page--front">
  <div class="hero-photo">
    <svg width="465" height="656" viewBox="0 0 465 656" role="img" aria-label="Foto: drei lachende Senioren winken und machen ein Selfie unter Bäumen">
      <defs>
        <linearGradient id="photoTone" x1="0" y1="0" x2="1" y2="1">
          <stop offset="0" stop-color="#6f8f5a"/>
          <stop offset="0.5" stop-color="#c9c3a6"/>
          <stop offset="1" stop-color="#e7e3d8"/>
        </linearGradient>
      </defs>
      <path d="M0 0 H465 V488 C330 540 170 570 0 574 Z" fill="url(#photoTone)"/>
    </svg>
  </div>
  <svg class="hero-bubble" width="465" height="656" viewBox="0 0 465 656">
    <path d="M295 349 C375 343 440 392 441 465 C442 535 385 572 318 571 C240 570 172 522 172 458 C172 395 225 354 295 349 Z" fill="#2580c8"/>
  </svg>
  <div class="headline headline__reiselust">Reiselust</div>
  <div class="headline headline__trotz">trotz</div>
  <div class="headline headline__pflegegrad">Pflegegrad</div>
  <div class="headline__rule"></div>
  <div class="headline headline__promise">wir machen es<br>möglich!</div>
  <div class="badge"><span class="badge__neu">Neu</span><br>ab Herbst<br>2025</div>

  <div class="footer">
    <div class="footer__dot"></div>
    <div class="footer__name">Sonnenweg Touren</div>
    <div class="footer__url">www.sonnenweg-touren.de</div>
  </div>
</section>

<section class="page page--back">
  <svg class="back-curve" width="465" height="656" viewBox="0 0 465 656">
    <path d="M0 574 C170 570 330 540 465 488 V656 H0 Z" fill="#ffffff"/>
  </svg>

  <div class="block" style="top:41px"><h2>Was wir bieten</h2></div>
  <ul class="offers">
    <li><svg width="11" height="9" viewBox="0 0 11 9"><path d="M1 4.5 L4 7.5 L10 1" stroke="#2580c8" stroke-width="2" fill="none"/></svg>Begleitung durch erfahrene Pflegefachkräfte</li>
    <li><svg width="11" height="9" viewBox="0 0 11 9"><path d="M1 4.5 L4 7.5 L10 1" stroke="#2580c8" stroke-width="2" fill="none"/></svg>Körperpflege, Medikamentengabe &amp; Betreuung wie zuhause</li>
    <li><svg width="11" height="9" viewBox="0 0 11 9"><path d="M1 4.5 L4 7.5 L10 1" stroke="#2580c8" stroke-width="2" fill="none"/></svg>24–Stunden-Erreichbarkeit unserer Pflegekräfte vor Ort im gebuchten Hotel</li>
    <li><svg width="11" height="9" viewBox="0 0 11 9"><path d="M1 4.5 L4 7.5 L10 1" stroke="#2580c8" stroke-width="2" fill="none"/></svg>Zusammenarbeit mit ausgewählten Hotels – barrierefrei &amp; seniorengerecht</li>
    <li><svg width="11" height="9" viewBox="0 0 11 9"><path d="M1 4.5 L4 7.5 L10 1" stroke="#2580c8" stroke-width="2" fill="none"/></svg>Kleine Gruppen &amp; individuelle Betreuung vor Ort</li>
  </ul>

  <div class="block" style="top:199px">
    <h2>Gut zu wissen</h2>
    <p>Für unsere pflegerische Begleitung entstehen Ihnen keine zusätzlichen Kosten, wenn Sie einen Pflegegrad haben und das Verhinderungspflege-Budget noch nicht aufgebraucht ist. Lediglich die Hotelkosten sind von Ihnen selbst zu tragen.</p>
  </div>

  <div class="block" style="top:286px">
    <h2>Wer hat Anspruch auf Verhinderungspflege?</h2>
    <p>Alle Pflegebedürftigen mit einem anerkannten Pflegegrad ab Stufe 2 können jährlich Verhinderungspflege über die Pflegekasse abrufen – ideal, um sich im Urlaub sicher begleiten zu lassen!</p>
  </div>

  <div class="block" style="top:358px">
    <h2>Unser Service – Ihr Mehrwert</h2>
    <p>Wir organisieren Ihre Reise von A bis Z und begleiten Sie oder Ihre Angehörigen auf dem Weg zu Erholung und neuen Eindrücken – mit Herz, Kompetenz und Erfahrung. Vor Ort sind müssen Sie auf nichts verzichten und werden versorgt wie zu Hause. Gerne organisieren wir auch die Abholung aus ihrer Häuslichkeit.</p>
  </div>

  <div class="block" style="top:461px">
    <h2>Sonnenweg Touren – Ihr verlässlicher<br>Partner für Pflege und Lebensfreude</h2>
  </div>

  <div class="contact">
    <div><span>Telefon:</span>0381 - 72946183</div>
    <div><span>E-Mail:</span>Mail@sonnenweg-touren .de</div>
  </div>

  <div class="cta">Jetzt<br>informieren<br>&amp; Platz<br>sichern!</div>

  <div class="footer">
    <div class="footer__dot"></div>
    <div class="footer__name">Sonnenweg Touren</div>
    <div class="footer__url">www.sonnenweg-touren.de</div>
  </div>
</section>

</body>
</html>
```